Design professional label for greener chemicals (cleaning and lubrication) brand

Design a b2b professional label that is based on the examples given.
Size: 135 x 200 mm, please use text of the label description doc (only the kaltro stainless steel polish example design document has the right text and size)
It should include:
1. Logo, can be fully changed except the shape of "KALTRO", colors and fonts of the rest can be customized
2. Focus should be on professional market, we would like to express the professionalism and high quality of the product
3. Focus should be on our brand name "KALTRO BRIGHTER COMPOUNDS"
4. Should include product name, product description, danger sentences, danger symbol, user instructions, image
5. Should include numbers that explain what the product does: 1. Prewash 2. Clean 3. Protect 4. Preserve and highlight number 2.

Target Market(s)

Professional cleaning companies, steel industry, food industry, pharmacy industry

Industry/Entity Type

Cleaning industry, steel industry, food industry, boat cleaning, car cleaning, professional lubrication

Font styles to use
Sans Serif

Requirements
Must have
• Professional look, clean look, image, focus on our brand name
Nice to have
• Numbers (see explanation), label divided in three parts (logo and product name and image in the middle as the highlight)

```html
<!DOCTYPE html>
<html lang="en">
<head>
<meta charset="utf-8">
<title>Kaltro Stainless Steel Polish – Label</title>
<link rel="stylesheet" href="https://fonts.googleapis.com/css2?family=Montserrat:wght@400;500;600;700;800&family=Russo+One&display=swap">
<style>
  :root {
    --navy: #0d1b3e;
    --navy-deep: #081330;
    --sky: #29a6de;
    --teal: #17788c;
    --brand: #1a5f86;
    --silver-1: #f4f5f6;
    --silver-2: #c9ccd0;
    --ink: #2c2c2c;
    --danger: #e2231a;
    --eco: #63b33b;
    --page: #f3f3f3;
  }
  * { box-sizing: border-box; margin: 0; padding: 0; }
  html, body { width: 900px; height: 1200px; overflow: hidden; }
  body {
    background: var(--page);
    font-family: "Montserrat", sans-serif;
    color: var(--ink);
    position: relative;
  }
  .label {
    position: absolute;
    left: 20px; top: 310px;
    width: 860px; height: 580px;
    background: #fff;
    box-shadow: 0 8px 18px rgba(0,0,0,.18);
  }
  /* ---------- front panel ---------- */
  .front {
    position: absolute; left: 0; top: 0;
    width: 548px; height: 580px;
    background: linear-gradient(90deg, var(--silver-2) 0%, var(--silver-1) 30%, #fff 50%, var(--silver-1) 70%, var(--silver-2) 100%);
    overflow: hidden;
  }
  .front-base {
    position: absolute; left: 0; top: 483px; width: 548px; height: 97px; background: #fff;
  }
  .eco-badge {
    position: absolute; left: 28px; top: 22px;
    width: 62px; height: 62px; border-radius: 50%;
    border: 3px solid var(--eco); background: #fff;
  }
  .brand-cap {
    position: absolute; left: 126px; top: -110px;
    width: 300px; height: 216px; border-radius: 50%;
    background: #fff;
    box-shadow: 0 2px 6px rgba(0,0,0,.12);
  }
  .brand-name {
    position: absolute; left: 126px; top: 34px; width: 300px;
    text-align: center;
    font-family: "Montserrat", sans-serif; font-weight: 800;
    font-size: 58px; letter-spacing: -1px; line-height: 1;
    color: var(--brand);
  }
  .teal-band {
    position: absolute; left: 0; top: 262px; width: 548px; height: 30px; background: var(--teal);
  }
  .title-plate { position: absolute; left: 74px; top: 118px; width: 394px; height: 174px; }
  .product-sub {
    position: absolute; left: 74px; top: 124px; width: 394px; text-align: center;
    font-weight: 500; font-size: 30px; color: var(--sky); letter-spacing: 1px; line-height: 1;
  }
  .product-name {
    position: absolute; left: 74px; top: 157px; width: 394px; text-align: center;
    font-family: "Russo One", sans-serif; font-size: 82px; line-height: 1; color: #fff; letter-spacing: 2px;
  }
  .product-claim {
    position: absolute; left: 74px; top: 245px; width: 394px; text-align: center;
    font-weight: 500; font-size: 17px; line-height: 20px; color: #fff; letter-spacing: 4px;
  }
  .collage { position: absolute; left: 0; top: 290px; width: 548px; height: 195px; }
  .steps {
    position: absolute; left: 0; top: 485px; width: 548px; height: 25px;
    background: var(--navy-deep); color: #fff;
    display: flex; justify-content: center; align-items: center; gap: 6px;
    font-weight: 500; font-size: 14px; letter-spacing: 4px;
  }
  .steps .step-highlight {
    background: var(--sky); border-radius: 11px; padding: 1px 6px 1px 10px; font-weight: 700;
  }
  .usage-intro {
    position: absolute; left: 0; top: 513px; width: 548px; text-align: center;
    font-size: 12px; color: #6b7f95; letter-spacing: .5px;
  }
  .usage-list {
    position: absolute; left: 0; top: 527px; width: 548px; text-align: center;
    font-size: 12.5px; font-weight: 700; color: var(--navy);
  }
  .usage-web {
    position: absolute; left: 0; top: 550px; width: 548px; text-align: center;
    font-size: 12px; color: #3c5a86; letter-spacing: .5px;
  }
  /* ---------- info panel ---------- */
  .info {
    position: absolute; left: 570px; top: 36px; width: 262px;
    font-size: 9.4px; line-height: 11.4px; color: #333;
  }
  .info h3 { font-size: 9.4px; font-weight: 600; color: var(--teal); margin-top: 10px; }
  .info p { margin: 0; }
  .info .lead { color: var(--teal); font-weight: 600; }
  .info .gap { margin-top: 8px; }
  .lot-table {
    position: absolute; left: 572px; top: 392px; width: 248px;
    border: 1.5px solid var(--navy); border-collapse: collapse;
    font-size: 7.5px; font-weight: 700; color: var(--navy);
  }
  .lot-table td { border: 1px solid var(--navy); height: 11px; padding: 0 3px; }
  .lot-table td:first-child { width: 78px; border-right: 1.5px solid var(--navy); }
  .hazard {
    position: absolute; left: 572px; top: 446px; width: 248px;
    font-size: 9.4px; line-height: 11.4px; color: #444; text-align: justify;
  }
  .hazard-icons { float: left; width: 50px; height: 46px; margin: 2px 4px 0 0; }
  .hazard strong { color: var(--danger); }
</style>
</head>
<body>
  <main class="label">
    <section class="front">
      <div class="front-base"></div>
      <div class="eco-badge" aria-hidden="true"></div>
      <div class="brand-cap"></div>
      <div class="brand-name">KALTRO</div>

      <div class="teal-band"></div>
      <svg class="title-plate" viewBox="0 0 394 174" aria-hidden="true">
        <path d="M38 0 H356 Q364 0 366 8 L370 34 H382 Q394 34 394 46 V160 Q394 174 380 174 H14 Q0 174 0 160 V46 Q0 34 12 34 H24 L28 8 Q30 0 38 0 Z" fill="var(--navy)"/>
      </svg>
      <div class="product-sub">STAINLESS STEEL</div>
      <div class="product-name">POLISH</div>
      <div class="product-claim">RESTORE STEEL SURFACES<br>HOLOGRAM FREE</div>

      <svg class="collage" viewBox="0 0 548 195">
        <defs>
          <linearGradient id="kitchen-tone" x1="0" y1="0" x2="1" y2="1">
            <stop offset="0" stop-color="#e6e8ea"/><stop offset="1" stop-color="#9ea3a8"/>
          </linearGradient>
          <linearGradient id="boat-tone" x1="0" y1="0" x2="1" y2="1">
            <stop offset="0" stop-color="#2f7fb5"/><stop offset=".5" stop-color="#c9bcb6"/><stop offset="1" stop-color="#1d5d8e"/>
          </linearGradient>
          <linearGradient id="glove-tone" x1="0" y1="0" x2="1" y2="1">
            <stop offset="0" stop-color="#8a8c90"/><stop offset=".5" stop-color="#e3c531"/><stop offset="1" stop-color="#b8b2a4"/>
          </linearGradient>
        </defs>
        <polygon points="0,0 140,0 168,195 0,195" fill="url(#kitchen-tone)" role="img" aria-label="Photo of a stainless steel industrial kitchen"/>
        <polygon points="146,0 480,0 448,195 174,195" fill="url(#boat-tone)" role="img" aria-label="Photo of a motor yacht cruising on blue water"/>
        <polygon points="486,0 548,0 548,195 454,195" fill="url(#glove-tone)" role="img" aria-label="Photo of a yellow-gloved hand polishing a steel hob"/>
      </svg>

      <div class="steps">
        <span>PREWASH</span><span class="step-highlight">CLEAN</span><span>PROTECT</span><span>PRESERVE</span>
      </div>
      <p class="usage-intro">AVAILABLE FOR</p>
      <p class="usage-list">BOATS | INDUSTRIAL STEEL SURFACES | STAINLESS STEEL KITCHEN</p>
      <p class="usage-web">WWW.KALTROCHEMICALS.COM</p>
    </section>

    <section class="info">
      <p><span class="lead">KALTRO stainless steel Polish</span> is a mildly abrasivecleansing cream with preservative properties. For removing stubborn dirt, water stains and deposits on stainless steel with a hologram free finish.Lustrex is non-tox and safe to use.</p>

      <h3>User instructions:</h3>
      <p>o Shake before use.</p>
      <p>o Apply with a damp brush, sponge or pad.</p>
      <p>o Adjust rubbing pressure and duration to the persistence of the soiling.</p>
      <p>o Add water as needed while rubbing, rub in the direction of the structure.</p>
      <p>o Rinse with clean water.</p>

      <h3>Expiring dates:</h3>
      <p>Batch number: see packaging.</p>
      <p>Net volume: see packaging.</p>

      <h3>Company information:</h3>
      <p>Produced by Kaltro Laboratories Int. B.V.</p>
      <p>Postbus 4821 - 7300 AK Deventer (NL)</p>
      <p>Phone NL: +31 570 12 34 56</p>
      <p>Lindenlaan 42 bus 3 – 3600 Genk (B)</p>
      <p>Phone B: +32 89 45 67 00</p>
      <p>www.kaltrochemicals.com</p>
      <p>hello@kaltrochemicals.com</p>
      <p class="gap">Label number: 23092021</p>
    </section>

    <table class="lot-table">
      <tr><td>EXPIRING DATES</td><td></td></tr>
      <tr><td>BATCH NUMBER</td><td></td></tr>
      <tr><td>NET VOLUME</td><td></td></tr>
    </table>

    <div class="hazard">
      <svg class="hazard-icons" viewBox="0 0 50 46" aria-label="Hazard pictograms">
        <g fill="#fff" stroke="var(--danger)" stroke-width="2">
          <rect x="17" y="2" width="16" height="16" transform="rotate(45 25 10)"/>
          <rect x="5" y="14" width="16" height="16" transform="rotate(45 13 22)"/>
          <rect x="29" y="14" width="16" height="16" transform="rotate(45 37 22)"/>
          <rect x="17" y="26" width="16" height="16" transform="rotate(45 25 34)"/>
        </g>
        <g fill="#222">
          <rect x="36" y="16" width="2" height="7"/><rect x="36" y="25" width="2" height="2"/>
        </g>
      </svg>
      <strong>Danger:</strong> Causes severe skin burns and eye damage. Wear protective gloves, protective clothing, eye protection, face protection. IF SWALLOWED: rinse mouth — DO NOT induce vomiting. Immediately call a POISON CENTER, a physician. IF ON SKIN (or hair): Take off immediately all contaminated clothing.
    </div>
  </main>
</body>
</html>
```